Header for Website

We need a header for our website that includes a simple logo. We will need to be able to seperate out the logo from the header to use on sales and marketing so we will also need this as a seperate file. We run an online sports platfom that covers several geographies and languages.

We need something simple but identifiable. Most of the sports we cover are team sports.

The company objectives are to use their community to crowdfund for projects and provide administration to help clubs run their teams and members.

Reason: I've extended this because of a holiday

Target Market(s)

Our target market will generally be men and women over the age of 40 who like team sports

Industry/Entity Type

Marketing

```html
<!DOCTYPE html>
<html lang="en">
<head>
<meta charset="utf-8">
<title>TeamKitty.net – Developing your club together</title>
<link rel="stylesheet" href="https://fonts.googleapis.com/css2?family=Source+Sans+3:wght@400;600;700&family=Oswald:wght@400&family=Arimo&display=swap">
<style>
:root{
  --navy:#1b1a6b;
  --band-a:#3b3d7a;
  --band-b:#7a7cae;
  --grass-a:#2e7d1f;
  --grass-b:#5fae3a;
  --form-green:#2f8a1f;
  --tab-blue:#0aa6e6;
  --tab-purple:#b43cc0;
  --tab-orange:#ef8a22;
  --accent-red:#cc1111;
  --field-border:#7a1a10;
  --btn-a:#ffa21a;
  --btn-b:#f07400;
  --banner-blue:#0d5fa8;
  --banner-light:#6fb0d8;
  --footer-bg:#efefef;
  --link-blue:#3a78c2;
  --heading-blue:#1e5fa0;
  --text:#111;
}
*{box-sizing:border-box;margin:0;padding:0}
html,body{width:1000px;height:1200px;overflow:hidden;background:#fff}
body{position:relative;font-family:"Source Sans 3",sans-serif;color:var(--text)}
.abs{position:absolute}

/* header */
.brand-name{left:216px;top:26px;font-size:37px;font-weight:400;color:var(--navy);letter-spacing:-.5px;line-height:1}
.brand-tag{left:366px;top:60px;font-size:9px;font-weight:600;color:var(--navy)}
.top-band{left:0;top:82px;width:1000px;height:287px;background:linear-gradient(135deg,var(--band-a),var(--band-b) 40%,var(--band-a) 70%,var(--band-b))}
.main-nav{left:215px;top:82px;height:36px;margin-top:8px;display:flex;align-items:center;z-index:2}
.main-nav a{color:#fff;text-decoration:none;font-size:15px;padding:0 16px;border-left:1px solid rgba(255,255,255,.7);line-height:24px}
.main-nav a:first-child{border-left:none}

/* content sheet */
.sheet{left:93px;top:369px;width:800px;height:500px;background:#fff;box-shadow:-8px 0 14px -6px rgba(60,60,120,.5),8px 0 14px -6px rgba(60,60,120,.5)}
.sheet-top{left:122px;top:130px;width:753px;height:239px;background:#fff}

.hero{left:130px;top:139px;width:737px;height:261px;background:radial-gradient(ellipse at 60% 40%,var(--grass-b),var(--grass-a))}
.hero-title{left:171px;top:208px;font-size:28px;color:#fff;line-height:1.25}
.hero-sub{left:171px;top:244px;font-size:26px;color:#111}
.hero-ball{left:482px;top:277px;width:160px;height:123px;border-radius:80px 80px 0 0;background:radial-gradient(circle at 50% 60%,#f3f3f3,#c9c9c9)}

.tab{left:660px;width:200px;height:82px;color:#fff;padding:14px 0 0 20px}
.tab h3{font-size:20px;font-weight:400;letter-spacing:.3px;line-height:1}
.tab p{font-size:11px;margin-top:8px;line-height:1.35;width:175px}
.tab.blue{top:145px;background:var(--tab-blue);border-left:7px solid var(--navy);padding-left:15px}
.tab.purple{top:228px;background:var(--tab-purple)}
.tab.orange{top:310px;background:var(--tab-orange);padding-left:18px}
.tab-pointer{left:652px;top:178px}

.intro1{left:0;width:1000px;top:425px;text-align:center;font-size:19px}
.intro2{left:191px;top:455px;font-size:19px}
.intro2 .free{color:var(--accent-red);font-size:29px}
.arrow{left:814px;top:466px}

/* register */
.register{left:100px;top:509px;width:775px;height:366px;background:var(--form-green)}
.video{left:127px;top:542px;width:413px;height:268px;background:#1a1a1a}
.video-screen{left:127px;top:558px;width:413px;height:222px;background:linear-gradient(160deg,#f6f6f6,#dedede);text-align:center;font-family:"Oswald",sans-serif;color:var(--heading-blue)}
.video-screen .v-title{font-size:42px;line-height:1;margin-top:8px;letter-spacing:1px}
.video-screen .v-sub{font-size:17px;margin-top:12px}
.video-screen .v-list{font-size:16px;line-height:25px;margin-top:22px}
.v-progress{left:127px;top:780px;width:413px;height:5px;background:#cc1a1a}
.v-time{left:201px;top:794px;font-family:"Arimo",sans-serif;font-size:9px;color:#fff}

.reg-title{left:603px;top:522px;font-size:20px;font-weight:600;color:#fff}
.field{left:596px;width:251px;height:30px;background:#fff;border:2px solid var(--field-border);border-radius:6px;font-size:12px;color:#444;padding:6px 0 0 12px}
.field-hint{left:608px;top:787px;font-size:12px;color:#fff}
.reg-btn{left:615px;top:824px;width:209px;height:37px;border-radius:6px;background:linear-gradient(var(--btn-a),var(--btn-b));border:2px solid #b34a00;color:#111;font-size:15px;text-align:center;line-height:33px}

/* banners */
.banner-left{left:123px;top:883px;width:463px;height:77px;background:linear-gradient(90deg,#a58a70 0,#c7a68a 30%,var(--banner-blue) 48%,var(--banner-blue))}
.banner-left span{position:absolute;left:214px;top:22px;font-size:21px;color:#fff;font-family:"Oswald",sans-serif;font-weight:400;letter-spacing:.3px}
.banner-right{left:599px;top:883px;width:277px;height:77px;background:linear-gradient(90deg,#d8b8a0 0,#c89e80 25%,var(--banner-light) 45%,var(--banner-light))}
.banner-right span{position:absolute;left:136px;top:13px;font-size:14px;line-height:17px;color:var(--navy);font-family:"Oswald",sans-serif;font-weight:400}

/* footer */
.footer{left:99px;top:967px;width:801px;height:189px;background:var(--footer-bg);border-top:1px solid #ddd}
.f-name{left:130px;top:1008px;font-size:19px;color:var(--navy)}
.f-tag{left:211px;top:1030px;font-size:5px;color:var(--navy)}
.f-stay{left:149px;top:1078px;font-size:17px;color:var(--heading-blue)}
.social{top:1109px;width:22px;height:21px;border-radius:4px;background:#6b6b6b;border:1px solid #333}
.f-head{top:1001px;font-size:17px;color:var(--heading-blue);display:flex;align-items:center;gap:8px}
.f-post{font-family:"Arimo",sans-serif;font-size:10.5px;line-height:13px;color:#222;width:190px}
.f-post small{display:block;font-size:7px;margin-top:4px;color:#222}
.f-post small em{font-style:normal;color:var(--link-blue)}
.f-contact{left:722px;top:1032px;font-family:"Arimo",sans-serif;font-size:10.5px;line-height:13px;color:var(--link-blue)}
.f-signup{left:727px;top:1092px;font-size:20px;line-height:21px;color:var(--navy)}
.bottom-bar{left:99px;top:1156px;width:801px;height:44px;background:linear-gradient(#3a3a3a,#1e1e1e);display:flex;align-items:center;padding-left:32px}
.bottom-bar a{color:#fff;text-decoration:none;font-size:13.5px;margin-right:28px}
.copyright{left:721px;top:1171px;font-family:"Arimo",sans-serif;font-size:9.5px;color:#bbb}
</style>
</head>
<body>

<!-- header -->
<div class="abs top-band" role="img" aria-label="Textured navy pattern"></div>
<div class="abs brand-name">TeamKitty.net</div>
<div class="abs brand-tag">Developing your club together</div>
<nav class="abs main-nav">
  <a href="#">Home</a><a href="#">About</a><a href="#">Our services</a><a href="#">Club Types</a><a href="#">News</a><a href="#">Information</a><a href="#">Contact</a>
</nav>

<!-- content sheet -->
<div class="abs sheet"></div>
<div class="abs sheet-top"></div>

<div class="abs hero" role="img" aria-label="Close-up of a grass football pitch"></div>
<div class="abs hero-ball" role="img" aria-label="Football resting on the grass"></div>
<div class="abs hero-title">We help your Raise funds</div>
<div class="abs hero-sub">Developing your club togerher</div>

<svg class="abs tab-pointer" width="10" height="18" viewBox="0 0 10 18"><path d="M10 0 L0 9 L10 18Z" fill="#1b1a6b"/></svg>
<div class="abs tab blue"><h3>FUNDRAISING</h3><p>Our online platform allows you to raise funds to</p></div>
<div class="abs tab purple"><h3>ADMIN</h3><p>Our online platform allows you to raise funds to</p></div>
<div class="abs tab orange"><h3>GOODS &amp; SERVICES</h3><p>Our online platform allows you to raise funds to</p></div>

<p class="abs intro1">Our online platform allows you to raise funds to buy equipment and develop your club.</p>
<p class="abs intro2">Watch the 2 minute video below and you can register for <span class="free">FREE below!</span></p>
<svg class="abs arrow" width="34" height="36" viewBox="0 0 34 36"><path d="M5 4 Q6 16 18 24" stroke="#1e5fa0" stroke-width="6" fill="none" stroke-linecap="round"/><path d="M12 28 L30 32 L26 14Z" fill="#1e5fa0"/></svg>

<!-- register -->
<section class="abs register"></section>
<div class="abs video"></div>
<div class="abs video-screen">
  <div class="v-title">TEAMKITTY</div>
  <div class="v-sub">WE HELP YOU:</div>
  <div class="v-list">RAISE FUNDS<br>ENGAGE WITH YOUR COMMUNITY<br>GET VALUE FOR YOUR CLUB</div>
</div>
<div class="abs v-progress"></div>
<svg class="abs" style="left:145px;top:792px" width="14" height="14"><path d="M2 1 L12 7 L2 13Z" fill="#ddd"/></svg>
<svg class="abs" style="left:174px;top:794px" width="14" height="10"><path d="M1 3 H4 L8 0 V10 L4 7 H1Z" fill="#ddd"/></svg>
<div class="abs v-time">0:00</div>
<svg class="abs" style="left:518px;top:793px" width="12" height="12"><path d="M1 4 V1 H4 M8 1 H11 V4 M11 8 V11 H8 M4 11 H1 V8" stroke="#ddd" fill="none" stroke-width="1.4"/></svg>

<div class="abs reg-title">Register here completely FREE!</div>
<div class="abs field" style="top:562px">First Name*</div>
<div class="abs field" style="top:608px">Last Name*</div>
<div class="abs field" style="top:657px">Club Name*</div>
<div class="abs field" style="top:706px">Email*</div>
<div class="abs field" style="top:755px">Club Type*</div>
<svg class="abs" style="left:825px;top:766px" width="12" height="8"><path d="M0 0 H12 L6 7Z" fill="#d2401a"/></svg>
<div class="abs field-hint">Pick the type that describes your club best</div>
<div class="abs reg-btn">Register Your Club Now</div>

<!-- banners -->
<div class="abs banner-left" role="img" aria-label="Smiling club supporter beside a blue panel"><span>ENGAGE WITH YOUR CLUB</span></div>
<div class="abs banner-right" role="img" aria-label="Fingers holding a coin beside a light blue panel"><span>USE YOUR<br>CONNECTIONSTO<br>DEVELOPYOUR CLUB</span></div>

<!-- footer -->
<footer class="abs footer"></footer>
<div class="abs f-name">TeamKitty.net</div>
<div class="abs f-tag">Developing your club together</div>
<div class="abs f-stay">Stay in Touch</div>
<div class="abs social" style="left:149px"></div>
<div class="abs social" style="left:186px"></div>
<div class="abs social" style="left:222px"></div>
<div class="abs social" style="left:259px"></div>
<div class="abs social" style="left:296px"></div>

<div class="abs f-head" style="left:356px">
  <svg width="12" height="12"><path d="M1 9 Q6 1 11 2 Q8 6 11 8 Q6 12 1 9Z" fill="#333"/></svg>Twiter Feed</div>
<div class="abs f-post" style="left:356px;top:1032px">Fully functioning Beginner Strategy EA10 seconds aronvelmark<small><em>33 minutes ago</em> by lanefield</small></div>
<div class="abs f-post" style="left:356px;top:1095px">Fully functioning Beginner Strategy EA10 seconds aronvelmark<small><em>33 minutes ago</em> by lanefield</small></div>

<div class="abs f-head" style="left:540px">
  <svg width="13" height="12"><path d="M0 0 H13 V8 H5 L2 11 V8 H0Z" fill="#333"/></svg>Testimonials</div>
<div class="abs f-post" style="left:541px;top:1032px">Fully functioning Beginner Strategy EA10 seconds aronvelmark<small><em>33 minutes ago</em> by lanefield</small></div>
<div class="abs f-post" style="left:541px;top:1096px">Fully functioning Beginner Strategy EA10 seconds aronvelmark<small><em>33 minutes ago</em> by lanefield</small></div>

<div class="abs f-head" style="left:721px">
  <svg width="10" height="13"><path d="M5 13 L1 6 A4 4 0 1 1 9 6Z" fill="#333"/><circle cx="5" cy="5" r="1.6" fill="#efefef"/></svg>Contact Us</div>
<div class="abs f-contact">48 Harbour Lane, Sydney AUS<br>Phone: 1800 555 0192</div>
<div class="abs f-signup">Sign up for<br>free now!</div>

<nav class="abs bottom-bar">
  <a href="#">Home</a><a href="#">About</a><a href="#">Our services</a><a href="#">Club Types</a><a href="#">News</a><a href="#">Information</a><a href="#">Contact</a>
</nav>
<div class="abs copyright">© TeamKitty.net All Rights Reserved.</div>

</body>
</html>
```